Web Design Project

We need the homepage and 7 interior pages designed as described below - design only:

Main Page
We like this template: http://www.quillbarrow.com/demo/52917.html

We also want a login dropdown similar to http://www.perloxa.com

We want the main page to be luxurious and sleek. We are a limo company that is dedicated to good service and creating an experience, and our front page should strongly reflect that. We do not want a very busy front page.

The main page should do primary things:

1. Make Reservations: We really like velmorta.com for this aspect of the site. That being said, velmorta is NOT the type of company we are.
2. Inform the customer of our most popular packages and give a sense of our professionalism and luxurious service.
3. There should be an area for a customer login
4. Menu should include the following: Home, Who We Are, Our Fleet, Custom Packages,
Testimonials, Book Your Ride!

For a starting point, we like this template http://www.quillbarrow.com/demo/52917.html

Rather than "start up, integrate, develop" we could have 3 of the more popular packages (or categories of packages). The bottom part would be fine. We could have a chirpnet feed, welcome, and our core principles. The one big change would be the addition of a "booking" area right smack in the middle of the page, where a customer could enter in trip data and see if the date was available.

-

About Us - Secondary Page
We like this ABOUT page template: http://www.quillbarrow.com/demo/63284.html

This is a really important page that people overlook, yet it is the most viewed page of a website after the homepage. We have come up with a bit of text to go on the about us page:

Who We Are: Brisbury Limo was founded on the core principle that every limo ride starts with personalized service from the instant you book your ride and continues after you step out of the car. You and your party are more than just our customers. We consider knowing your name and providing you with your choice of snacks and periodicals in the car just a few of the integral elements of the limousine experience. We are striving to revolutionize the limousine industry by creating a personal, friendly, timely, and professional experience. Brisbury Limo combines current technology and a modern fleet with good old-fashioned service to deliver you a personalized, luxury experience. We cater to every event, from business travel to proms and wedding, and everything in between.

We do all of this while maintaining competitive pricing to our peers.

Have a taste of high society...

-

Custom Packages - Secondary Page

This page will contain descriptions of the packages that we offer: Wedding, Prom, Business, etc. - there should be a thumbnail of each package with a description next to it. When you click on a thumbnail it will bring you to a detailed page of that particular package.

-

Custom Packages Interior Page - Secondary Page

In depth look at that particular package - for example, weddings - shows that we offer complimentary champagne, Just married sign, etc.

-

Fleet Page - Secondary Page

This page can be fairly basic. It will include photos of the vehicles along with descriptions and number of passengers, etc.

-

Testimonials Page - Secondary Page

This page will have testimonials from customers. We don't want a big block of text, but rather small testimonials that will expand within the page when you click on a "+" symbol. We like the way it looks when the testimonials are enclosed within a speech bubble image - still professional and classy, not cheesy.

-

Book your ride! - Secondary Page

This page will have a form on it - the same as the form on the homepage, where people can enter in information to check the availability of vehicles. We also want basic contact information on this page as well in case people want to call directly or e-mail.

Requirements
Must have
• - Book your reservation form on homepage
- Sleek, elegant feel
- Chirpnet feed

```html
<!DOCTYPE html>
<html lang="en">
<head>
<meta charset="utf-8">
<title>Brisbury Limo — Home</title>
<link rel="stylesheet" href="https://fonts.googleapis.com/css2?family=Source+Sans+3:wght@300;400;600;700&display=swap">
<style>
:root{
  --navy:#0b2a82;
  --royal:#0a5ab8;
  --sky:#1a7fd6;
  --panel:#0d3f9a;
  --panel-dark:#0b2c86;
  --gold:#f5a400;
  --ink:#2b2b2b;
  --bubble:#3a3a3a;
  --paper:#ececec;
  --white:#ffffff;
  --font:"Source Sans 3",Arial,sans-serif;
}
*{box-sizing:border-box;margin:0;padding:0}
html,body{width:1200px;height:1169px;overflow:hidden}
body{font-family:var(--font);background:var(--paper);position:relative;color:var(--white)}
.abs{position:absolute}

.hero{left:0;top:0;width:1200px;height:515px;
  background:radial-gradient(ellipse 700px 420px at 560px 30px,#1d8ee6 0%,#0a58b8 45%,#0b2f8e 100%)}
.hero-band{left:0;top:100px;width:1200px;height:41px;background:rgba(20,90,190,.55)}
.brand{font-weight:400;font-size:26px;color:var(--white);line-height:1;white-space:nowrap}
.brand-head{left:175px;top:48px}
.call{left:772px;top:6px;font-size:25px;font-weight:400}
.search{left:818px;top:56px;width:210px;height:28px;background:var(--white);border-radius:3px;color:#999;font-size:12px;padding:7px 10px}
.search svg{position:absolute;right:7px;top:5px}

.link-tab{left:179px;top:104px;width:63px;height:26px;background:#1c1c1f;font-size:16px;padding:6px 0 0 14px;border-radius:3px 3px 0 0}
.nav{left:179px;top:126px;width:819px;height:88px;background:linear-gradient(#232326,#151517);border-radius:0 3px 3px 3px;display:flex;padding-left:55px}
.nav-item{height:88px;display:flex;flex-direction:column;align-items:center;justify-content:flex-end;padding-bottom:10px;font-size:13px;text-transform:uppercase;border-right:1px solid #333;gap:7px}
.nav-item:last-child{border-right:0}

.slide-base{left:225px;top:470px;width:748px;height:36px;background:#0a2570}
.slide-frame{left:234px;top:180px;width:731px;height:316px;background:var(--white);border-radius:4px;box-shadow:0 2px 8px rgba(0,0,0,.4)}
.slide-photo{left:240px;top:214px;width:717px;height:274px;
  background:linear-gradient(100deg,#bfbfae 0%,#6d6a52 25%,#2a2a22 45%,#8b8b80 65%,#2e2e2e 85%,#5a4a48 100%)}
.cap1{left:240px;top:214px;width:180px;height:36px;background:rgba(40,40,40,.75);font-size:23px;padding:4px 0 0 6px}
.cap2{left:320px;top:258px;width:128px;height:34px;background:rgba(40,40,40,.75);font-size:23px;padding:3px 0 0 10px}
.arrow{width:50px;height:50px;border-radius:50%;background:#0a2672;display:flex;align-items:center;justify-content:center}
.arrow span{width:32px;height:32px;border-radius:50%;background:#eee;display:flex;align-items:center;justify-content:center}

.card{top:524px;width:278px;height:352px;box-shadow:0 10px 10px -6px rgba(30,110,210,.5)}
.card-head{height:48px;display:flex;align-items:center;justify-content:center;font-size:23px}
.card-head b{color:var(--gold);font-weight:700}
.book{left:166px;background:linear-gradient(#0e5bb5,#0b3f9c)}
.book .card-head{background:rgba(0,0,0,.08)}
.radios{display:flex;gap:14px;font-size:13px;margin:12px 0 0 17px;align-items:center}
.radio{width:14px;height:14px;border-radius:50%;background:var(--white);display:inline-block;margin-right:9px;vertical-align:-2px}
.radio.on{box-shadow:inset 0 0 0 3px var(--white),inset 0 0 0 7px #0c4fa8}
.multi{margin:12px 0 0 19px;width:103px;height:21px;background:#1d3e94;color:#6f95d8;font-size:13px;padding:2px 0 0 9px;border-radius:2px}
.label{font-size:13px;margin-left:20px}
.field{background:var(--white);height:22px;border-radius:3px}
.calc{left:48px;top:277px;width:177px;height:39px;background:linear-gradient(#fff,#dcdcdc);border-radius:3px;color:#1a3a85;font-weight:700;font-size:21px;text-align:center;line-height:38px;letter-spacing:-.6px}
.guarantee{left:0;width:278px;top:320px;text-align:center;font-size:13px}

.packs{left:462px;background:linear-gradient(#0d3796,#0b2b86)}
.packs .card-head{justify-content:flex-start;padding-left:37px;background:rgba(255,255,255,.04)}
.popular{right:7px;top:4px;font-size:11px}
.pack{left:11px;width:260px;height:80px}
.pack-img{width:106px;height:74px}
.pack-text{left:116px;top:0;width:143px;font-size:11.6px;line-height:14.2px;text-align:justify}
.pack-link{right:0;top:63px;color:var(--gold);font-size:14px}

.who{left:758px;background:linear-gradient(#0d3796,#0b2b86)}
.who-img{left:9px;top:52px;width:257px;height:112px;background:linear-gradient(#b88c1e 0%,#f2c640 30%,#9b6b12 55%,#1b1b1b 75%,#cfcfc8 100%)}
.who-text{left:13px;top:170px;width:253px;font-size:11.6px;line-height:14.4px;text-align:justify}
.more{left:197px;top:306px;width:66px;height:26px;background:linear-gradient(#fff,#ddd);border-radius:3px;color:#1a3a85;font-size:16px;text-align:center;line-height:25px}

.t-title{left:179px;top:897px;font-size:19px;color:var(--ink);font-weight:400}
.bubble{left:175px;top:931px;width:851px;height:74px;background:var(--bubble);border-radius:3px;color:#ddd;font-size:15px;text-align:center;padding:16px 40px 0;line-height:17px}
.bubble-tail{left:949px;top:1004px}
.author{left:790px;top:1018px;width:111px;text-align:right;color:#333;font-size:10.5px;line-height:13px}
.author b{font-weight:600}
.avatar{left:910px;top:1013px;width:33px;height:37px;background:linear-gradient(#cfd8c4,#3c6d3a)}

.footer{left:0;top:1065px;width:1200px;height:104px;background:radial-gradient(ellipse 600px 200px at 560px 104px,#1a7fd6 0%,#0b49a8 50%,#0a2d8d 100%)}
.f-nav{left:168px;top:22px;display:flex;gap:26px;font-size:13px;text-transform:uppercase}
.follow{left:171px;top:72px;font-size:13px;display:flex;align-items:center;gap:8px}
.social{width:28px;height:28px;border-radius:50%;background:#f2f2f2;box-shadow:0 2px 3px rgba(0,0,0,.3);display:inline-block}
.brand-foot{left:808px;top:42px}
.copy{left:880px;top:80px;font-size:11px}
</style>
</head>
<body>

<section class="hero abs"></section>
<div class="hero-band abs"></div>

<div class="brand brand-head abs">Brisbury Limo</div>
<div class="call abs">Call us : 001 047 . 369 41</div>
<div class="search abs">Search
  <svg width="18" height="18" viewBox="0 0 18 18"><circle cx="10.5" cy="7.5" r="5.5" fill="none" stroke="#bbb" stroke-width="1.6"/><path d="M6.5 11.5 2 16" stroke="#bbb" stroke-width="2"/></svg>
</div>

<div class="slide-base abs"></div>
<div class="slide-frame abs"></div>
<div class="slide-photo abs" role="img" aria-label="Limousine interior with lit bar, glassware and leather seating"></div>
<div class="cap1 abs">HIGH SOCIETY</div>
<div class="cap2 abs">LOW PRICE</div>

<div class="link-tab abs">LINK</div>
<nav class="nav abs">
  <div class="nav-item" style="width:86px">
    <svg width="26" height="24" viewBox="0 0 26 24"><path d="M13 1 1 12h4v11h6v-7h4v7h6V12h4z" fill="#fff"/></svg>Home</div>
  <div class="nav-item" style="width:130px">
    <svg width="24" height="27" viewBox="0 0 24 27"><rect x="1" y="1" width="22" height="22" rx="2" fill="#fff"/><circle cx="12" cy="9" r="4" fill="#1b1b1b"/><path d="M5 20c1-5 13-5 14 0z" fill="#1b1b1b"/><path d="M9 23h6l-3 3z" fill="#fff"/></svg>Who We Are</div>
  <div class="nav-item" style="width:113px">
    <svg width="40" height="26" viewBox="0 0 40 26"><rect x="2" y="6" width="20" height="11" fill="#fff"/><path d="M22 9h8l5 5v3H22z" fill="#fff"/><circle cx="9" cy="19" r="3" fill="#fff"/><circle cx="29" cy="19" r="3" fill="#fff"/><path d="M2 24h36" stroke="#fff" stroke-width="1.5" stroke-dasharray="5 3"/><rect x="8" y="1" width="8" height="5" fill="#fff"/></svg>Our Fleet</div>
  <div class="nav-item" style="width:183px">
    <svg width="22" height="30" viewBox="0 0 22 30"><path d="M3 8 11 1l8 7-2 20H5z" fill="#fff" transform="rotate(-25 11 15)"/><circle cx="9" cy="7" r="2" fill="#1b1b1b"/></svg>Custom Packages</div>
  <div class="nav-item" style="width:130px">
    <svg width="24" height="30" viewBox="0 0 24 30"><rect x="1" y="1" width="22" height="28" fill="none" stroke="#fff" stroke-width="2"/><path d="M5 8h14M5 12h14M5 16h14M5 20h14M5 24h10" stroke="#fff" stroke-width="2"/></svg>Testimonials</div>
  <div class="nav-item" style="width:140px">
    <svg width="26" height="22" viewBox="0 0 26 22"><path d="M13 21 2 10C-2 4 6-2 13 5c7-7 15-1 11 5z" fill="#fff"/></svg>Book Your Ride!</div>
</nav>

<div class="arrow abs" style="left:166px;top:317px"><span><svg width="10" height="12" viewBox="0 0 10 12"><path d="M7 1 2 6l5 5" fill="none" stroke="#777" stroke-width="2"/></svg></span></div>
<div class="arrow abs" style="left:983px;top:317px"><span><svg width="10" height="12" viewBox="0 0 10 12"><path d="M3 1l5 5-5 5" fill="none" stroke="#777" stroke-width="2"/></svg></span></div>

<section class="card book abs">
  <div class="card-head">Book Your Ride!&nbsp;<b>NOW</b></div>
  <div class="radios"><span><i class="radio on"></i>One way</span><span><i class="radio"></i>By The Hour</span></div>
  <div class="multi">Multiple Rides ❯</div>
  <div class="label" style="margin-top:8px">I want to be picked up at:</div>
  <div class="field abs" style="left:19px;top:140px;width:241px"></div>
  <div class="label abs" style="left:0;top:172px">...and dropped off at:</div>
  <div class="field abs" style="left:19px;top:189px;width:241px"></div>
  <div class="label abs" style="left:2px;top:221px">Pickup Date</div>
  <div class="label abs" style="left:123px;top:221px">Pickup Time</div>
  <div class="field abs" style="left:19px;top:242px;width:103px"></div>
  <div class="field abs" style="left:141px;top:242px;width:56px"></div>
  <div class="field abs" style="left:202px;top:242px;width:56px"></div>
  <div class="calc abs">Calculate Price</div>
  <div class="guarantee abs">Guaranteed on Time</div>
</section>

<section class="card packs abs">
  <div class="popular abs">Popular</div>
  <div class="card-head">Packages to&nbsp;<b>customers</b></div>
  <div class="pack abs" style="top:58px">
    <div class="pack-img" role="img" aria-label="Limousine cabin with beige leather seats" style="background:linear-gradient(#3a3530,#b3a48c,#3a3530)"></div>
    <p class="pack-text abs">Lorem ipsum dolor sit amet, consectetur adipisicing elit, sed do eiusmod tempor incididunt aveniam,</p>
    <span class="pack-link abs">Price Details</span>
  </div>
  <div class="pack abs" style="top:148px">
    <div class="pack-img" role="img" aria-label="Limousine interior with blue ambient lighting" style="background:linear-gradient(#1a2f6a,#8ba7d8,#1a2f6a)"></div>
    <p class="pack-text abs">Lorem ipsum dolor sit amet, consectetur adipisicing elit, sed do eiusmod tempor incididunt aveniam,</p>
    <span class="pack-link abs">Price Details</span>
  </div>
  <div class="pack abs" style="top:243px">
    <div class="pack-img" role="img" aria-label="Party bus interior with neon lights" style="background:linear-gradient(#1a1520,#6a4c7a,#1a1520)"></div>
    <p class="pack-text abs">Lorem ipsum dolor sit amet, consectetur adipisicing elit, sed do eiusmod tempor incididunt aveniam,</p>
    <span class="pack-link abs">Price Details</span>
  </div>
</section>

<section class="card who abs">
  <div class="card-head">Who we are ?</div>
  <div class="who-img abs" role="img" aria-label="Black stretch limousine parked in front of a lit building at night"></div>
  <p class="who-text abs">Lorem ipsum dolor sit amet, consectetur adipisicing elit, sed do eiusmod tempor incididunt aveniam, Sed ut perspiciatis unde omnis iste natus error sit voluptatem accusantium doloremque laudantium, totam rem aperiam, eaque ipsa quae ab illo inventore veritatis et quasi architecto beatae vitae dicta sunt explicabo. Nemo enim ipsam voluptatem quia voluptas sit aspernatur aut odit aut fugit, sed quia consequuntur magni dolores eos qui</p>
  <div class="more abs">More</div>
</section>

<h2 class="t-title abs">Testimonials</h2>
<blockquote class="bubble abs">I just purchased and am so excited about this theme! The admin is so incredible! Thanks Marisol, I have given you 5 stars for your excellent support! Cheers!</blockquote>
<svg class="bubble-tail abs" width="30" height="30" viewBox="0 0 30 30"><path d="M0 0h30L0 28z" fill="var(--bubble)"/></svg>
<div class="author abs"><b>Dale Whitcombe</b><br>Company Name</div>
<div class="avatar abs" role="img" aria-label="Customer portrait"></div>

<footer class="footer abs">
  <div class="f-nav abs"><span>Home</span><span>Who We Are</span><span>Our Fleet</span><span>Custom Packages</span><span>Testimonials</span><span>Book Your Ride!</span></div>
  <div class="follow abs">FOLLOW US ON :&nbsp;<i class="social"></i><i class="social"></i><i class="social"></i><i class="social"></i></div>
  <div class="brand brand-foot abs">Brisbury Limo</div>
  <div class="copy abs">© 2012.www.Brisburylimo.com</div>
</footer>

</body>
</html>
```